Law Office needs stationery design and business card

I currently have been using the same letterhead for the last 8 years. Since i 'm about to adding another location, I want to revamp my letterhead and business card. I already have a logo i'm happy with. I will upload my current letterhead, fax sheet, envelope, and logos. I need a business card also. I have 2 locations, 1 phone number, 1 fax line, website, etc. If possible and fitting with the design, I would like to keep the same information listed currently on the letterhead.

**Keep in mind, I also NEED A FAX SHEET COVER. thank you

Hello, Please submit a Gray Scale or Black and White version of your designs also, since most of the time I will be printing NON color stationery. I will seldom use a color print for my letterhead, I would like to have a color version for my benefit, however i will print in grayscale majority of the time . For the Business Card, that can just be in color. When I get my business cards they will be in color.Thank youEnrique Added Sunday, September 18, 2016

```html
<!DOCTYPE html>
<html lang="en">
<head>
<meta charset="utf-8">
<title>Marbrook Law Letterhead</title>
<link href="https://fonts.googleapis.com/css2?family=Cinzel:wght@400&family=Open+Sans:ital,wght@0,400;1,700&display=swap" rel="stylesheet">
<style>
  :root{
    --paper:#fdf9f1;
    --band:#f5e6c0;
    --tile-mid:#ede0c6;
    --tile-light:#faf1dc;
    --gold:#b8985a;
    --gold-deep:#c4a464;
    --ink:#2b2b2b;
    --faint:#d8d4cc;
    --diamond:#f5eddc;
  }
  html,body{margin:0;padding:0;overflow:hidden;}
  body{width:849px;height:1200px;background:var(--paper);}
  .letterhead{position:relative;width:849px;height:1200px;overflow:hidden;background:var(--paper);font-family:"Open Sans",sans-serif;color:var(--ink);}
  .header-band{position:absolute;left:0;top:55px;width:308px;height:31px;background:var(--band);}
  .brand-square{position:absolute;left:128px;top:40px;width:38px;height:38px;background:var(--gold);}
  .brand-name{position:absolute;left:58px;top:103px;margin:0;font-family:"Cinzel",serif;font-weight:400;font-size:20px;letter-spacing:0.5px;color:var(--gold);}
  .attorney-line{position:absolute;left:77px;top:134px;margin:0;font-style:italic;font-weight:700;font-size:14px;color:var(--gold);}
  .corner-pattern{position:absolute;left:660px;top:0;width:189px;height:214px;border-bottom-left-radius:4px;background:linear-gradient(150deg,var(--tile-mid) 0%,var(--tile-light) 70%,var(--paper) 100%);}
  .watermark-diamond{position:absolute;left:304px;top:480px;width:240px;height:240px;background:var(--diamond);transform:rotate(45deg);}
  .watermark-name{position:absolute;left:0;top:582px;width:849px;text-align:center;margin:0;font-family:"Cinzel",serif;font-size:34px;color:var(--faint);letter-spacing:1px;}
  .contact{position:absolute;top:1068px;font-size:12.6px;line-height:20.7px;}
  .contact ul{list-style:none;margin:0;padding:0;}
  .contact li{position:relative;padding-left:16px;white-space:nowrap;}
  .contact svg{position:absolute;left:0;top:4px;width:12px;height:12px;}
  .col-address{left:36px;}
  .col-phone{left:249px;}
  .col-staff-a{left:419px;}
  .col-staff-b{left:619px;}
  .divider{position:absolute;top:1068px;width:1px;height:78px;background:var(--gold);opacity:.6;}
  .footer-bands{position:absolute;left:0;top:1186px;width:849px;height:14px;}
</style>
</head>
<body>
<div class="letterhead">
  <div class="header-band"></div>
  <div class="brand-square"></div>
  <p class="brand-name">MARBROOK LAW</p>
  <p class="attorney-line">Gustavo Marbrook Esq.</p>

  <div class="corner-pattern" role="img" aria-label="Decorative pattern of soft beige squares in the top corner"></div>

  <div class="watermark-diamond"></div>
  <p class="watermark-name">MARBROOK LAW</p>

  <div class="contact col-address"><ul>
    <li><svg viewBox="0 0 12 12"><circle cx="6" cy="6" r="5.3" fill="none" stroke="var(--gold)"/><path d="M6 3a2 2 0 0 1 2 2c0 1.5-2 4-2 4S4 6.5 4 5a2 2 0 0 1 2-2z" fill="var(--gold)"/></svg>48 East Elm St., Suite 300,</li>
    <li>Linden, PA 19081</li>
    <li><svg viewBox="0 0 12 12"><circle cx="6" cy="6" r="5.3" fill="none" stroke="var(--gold)"/><path d="M6 3a2 2 0 0 1 2 2c0 1.5-2 4-2 4S4 6.5 4 5a2 2 0 0 1 2-2z" fill="var(--gold)"/></svg>730 Chestnut Ave, Fairmont,</li>
    <li>PA 19422</li>
  </ul></div>
  <div class="divider" style="left:241px"></div>

  <div class="contact col-phone"><ul>
    <li><svg viewBox="0 0 12 12"><circle cx="6" cy="6" r="5.3" fill="none" stroke="var(--gold)"/><path d="M4.3 3.2c-.6.4-.7 1.3.1 2.6s1.8 2 2.6 2.1c.5 0 .9-.3 1-.7L7 6.5l-.6.4c-.5-.2-1-.8-1.2-1.3l.4-.6z" fill="var(--gold)"/></svg>610.555.0142</li>
    <li><svg viewBox="0 0 12 12"><circle cx="6" cy="6" r="5.3" fill="none" stroke="var(--gold)"/><rect x="3.5" y="5" width="5" height="3" fill="none" stroke="var(--gold)" stroke-width=".8"/><rect x="4.5" y="3.3" width="3" height="1.7" fill="var(--gold)"/></svg>484.555.0187</li>
    <li><svg viewBox="0 0 12 12"><circle cx="6" cy="6" r="5.3" fill="none" stroke="var(--gold)"/><circle cx="6" cy="6" r="3" fill="none" stroke="var(--gold)" stroke-width=".8"/><path d="M3 6h6M6 3v6" stroke="var(--gold)" stroke-width=".6"/></svg>www.MarbrookLaw.com</li>
    <li><svg viewBox="0 0 12 12"><circle cx="6" cy="6" r="5.3" fill="none" stroke="var(--gold)"/></svg>MarbrookLaw</li>
  </ul></div>
  <div class="divider" style="left:413px"></div>

  <div class="contact col-staff-a"><ul>
    <li><svg viewBox="0 0 12 12"><path d="M3 1.5l7 4.5-7 4.5z" fill="var(--gold)"/></svg>Gustavo Marbrook Esq.</li>
    <li><svg viewBox="0 0 12 12"><circle cx="6" cy="6" r="5.3" fill="none" stroke="var(--gold)"/><rect x="3.2" y="4" width="5.6" height="4" fill="none" stroke="var(--gold)" stroke-width=".7"/><path d="M3.2 4L6 6.3 8.8 4" fill="none" stroke="var(--gold)" stroke-width=".7"/></svg>Gustavo@MarbrookLaw.com</li>
    <li><svg viewBox="0 0 12 12"><path d="M3 1.5l7 4.5-7 4.5z" fill="var(--gold)"/></svg>Nadia Kowalczyk Esq.</li>
    <li><svg viewBox="0 0 12 12"><circle cx="6" cy="6" r="5.3" fill="none" stroke="var(--gold)"/><rect x="3.2" y="4" width="5.6" height="4" fill="none" stroke="var(--gold)" stroke-width=".7"/><path d="M3.2 4L6 6.3 8.8 4" fill="none" stroke="var(--gold)" stroke-width=".7"/></svg>Nadia@MarbrookLaw.com</li>
  </ul></div>
  <div class="divider" style="left:612px"></div>

  <div class="contact col-staff-b"><ul>
    <li><svg viewBox="0 0 12 12"><path d="M3 1.5l7 4.5-7 4.5z" fill="var(--gold)"/></svg>Claire Dunmore Esq.</li>
    <li><svg viewBox="0 0 12 12"><circle cx="6" cy="6" r="5.3" fill="none" stroke="var(--gold)"/><rect x="3.2" y="4" width="5.6" height="4" fill="none" stroke="var(--gold)" stroke-width=".7"/><path d="M3.2 4L6 6.3 8.8 4" fill="none" stroke="var(--gold)" stroke-width=".7"/></svg>Claire@MarbrookLaw.com</li>
    <li><svg viewBox="0 0 12 12"><path d="M3 1.5l7 4.5-7 4.5z" fill="var(--gold)"/></svg>Owen Hartley Esq. of counsel</li>
    <li><svg viewBox="0 0 12 12"><circle cx="6" cy="6" r="5.3" fill="none" stroke="var(--gold)"/><rect x="3.2" y="4" width="5.6" height="4" fill="none" stroke="var(--gold)" stroke-width=".7"/><path d="M3.2 4L6 6.3 8.8 4" fill="none" stroke="var(--gold)" stroke-width=".7"/></svg>Owen@MarbrookLaw.com</li>
  </ul></div>

  <svg class="footer-bands" viewBox="0 0 849 14" preserveAspectRatio="none">
    <polygon points="0,0 210,0 205,14 0,14" fill="var(--band)"/>
    <polygon points="222,0 849,0 849,14 217,14" fill="var(--gold-deep)"/>
  </svg>
</div>
</body>
</html>
```